Personal Development Brand Needs a Workbook Cover Design

We need a clean and sleek cover design for our A4-Sized workbook called the "Lantern Path Journal Set"

There's around 90 pages in the workbook, if that matters for the spine.

Necessary Elements on the Front Cover:

- Logo
- Title: Keen Crest Lantern Path Journal
- Subtitle: A Simple Workbook to Track Your Transformation
- Author Name: Dorian Pellow

Elements on Back Cover:

- The Keen Crest Charter

```html
<!DOCTYPE html>
<html lang="en">
<head>
<meta charset="utf-8">
<title>Keen Crest Lantern Path Journal – Cover Wrap</title>
<link href="https://fonts.googleapis.com/css2?family=Bebas+Neue&family=Lato:wght@700;900&family=Montserrat:wght@600&display=swap" rel="stylesheet">
<style>
  :root {
    --paper-light: #f7f7f8;
    --paper-mid: #e4e5e7;
    --paper-dark: #c9cacc;
    --ink: #111111;
    --crest-red: #e31e26;
    --spine: #0b0b0b;
    --white: #ffffff;
  }
  * { margin: 0; padding: 0; box-sizing: border-box; }
  html, body { width: 1200px; height: 839px; overflow: hidden; background: var(--paper-light); }
  .cover-wrap {
    position: relative;
    width: 1200px;
    height: 839px;
    overflow: hidden;
    background: radial-gradient(ellipse 70% 80% at 60% 60%, var(--paper-light) 0%, var(--paper-mid) 65%, var(--paper-dark) 100%);
  }
  .figure-art {
    position: absolute;
    left: 415px;
    top: 28px;
    width: 385px;
    height: 780px;
    background: radial-gradient(ellipse 40% 50% at 50% 45%, rgba(138,138,138,0.55) 0%, rgba(138,138,138,0.25) 55%, rgba(138,138,138,0) 100%);
  }
  .spine {
    position: absolute;
    left: 596px;
    top: 0;
    width: 15px;
    height: 839px;
    background: var(--spine);
  }
  .spine-text {
    position: absolute;
    left: 0;
    width: 15px;
    writing-mode: vertical-rl;
    text-align: center;
    line-height: 15px;
    white-space: nowrap;
  }
  .spine-brand { top: 78px; font-family: 'Bebas Neue', sans-serif; font-size: 14px; letter-spacing: 1px; color: var(--white); }
  .spine-title { top: 160px; font-family: 'Bebas Neue', sans-serif; font-size: 14px; letter-spacing: 3px; color: var(--crest-red); }
  .spine-author { top: 622px; font-family: 'Montserrat', sans-serif; font-weight: 600; font-size: 10px; letter-spacing: 4px; color: var(--white); }

  .charter { position: absolute; left: 136px; top: 200px; width: 308px; text-align: center; }
  .charter-heading {
    height: 40px;
    background: var(--crest-red);
    color: var(--white);
    font-family: 'Bebas Neue', sans-serif;
    font-size: 28px;
    line-height: 42px;
    letter-spacing: 0.5px;
    font-weight: 400;
  }
  .charter-list { list-style: none; margin-top: 23px; }
  .charter-list li {
    font-family: 'Lato', sans-serif;
    font-weight: 900;
    font-size: 17px;
    line-height: 18px;
    color: var(--ink);
    margin-bottom: 17px;
  }

  .front-title {
    position: absolute;
    left: 690px;
    top: 140px;
    width: 440px;
    text-align: center;
    font-family: 'Bebas Neue', sans-serif;
    font-weight: 400;
    line-height: 1;
  }
  .title-brand { display: block; font-size: 112px; color: var(--ink); height: 98px; letter-spacing: 1px; }
  .title-line { display: block; font-size: 80px; color: var(--crest-red); height: 76px; letter-spacing: 2px; }
  .title-main { display: block; font-size: 150px; color: var(--crest-red); letter-spacing: 2px; }

  .front-subtitle {
    position: absolute;
    left: 700px;
    top: 462px;
    width: 420px;
    text-align: center;
    font-family: 'Lato', sans-serif;
    font-weight: 700;
    font-size: 18px;
    color: var(--ink);
  }

  .brand-mark {
    position: absolute;
    left: 700px;
    top: 690px;
    width: 420px;
    display: flex;
    justify-content: center;
    align-items: center;
    gap: 10px;
    font-family: 'Bebas Neue', sans-serif;
    font-size: 26px;
    letter-spacing: 1px;
    color: var(--ink);
  }
  .brand-square { width: 20px; height: 20px; background: var(--crest-red); }

  .front-author {
    position: absolute;
    left: 700px;
    top: 760px;
    width: 420px;
    text-align: center;
    font-family: 'Montserrat', sans-serif;
    font-weight: 600;
    font-size: 21px;
    letter-spacing: 8px;
    color: var(--ink);
  }
</style>
</head>
<body>
<main class="cover-wrap">
  <section class="back-cover">
    <div class="charter">
      <h2 class="charter-heading">THE KEEN CREST CHARTER</h2>
      <ul class="charter-list">
        <li>We do things that matter.</li>
        <li>We are skeptical of our limits.</li>
        <li>We don't fear mistakes,<br>only mediocrity.</li>
        <li>We don't just think positive<br>thoughts, we act on them.</li>
        <li>We know our most important<br>skill is the ability to dream<br>beyond our current abilities.</li>
      </ul>
    </div>
  </section>

  <div class="figure-art" role="img" aria-label="Grey wireframe polygon-mesh illustration of a standing human figure spanning back cover, spine and front cover"></div>

  <aside class="spine">
    <span class="spine-text spine-brand">KEEN CREST</span>
    <span class="spine-text spine-title">LANTERN PATH JOURNAL</span>
    <span class="spine-text spine-author">DORIAN PELLOW</span>
  </aside>

  <section class="front-cover">
    <h1 class="front-title">
      <span class="title-brand">KEEN CREST</span>
      <span class="title-line">LANTERN PATH</span>
      <span class="title-main">JOURNAL</span>
    </h1>
    <p class="front-subtitle">A Simple Workbook to Track Your Transformation</p>
    <div class="brand-mark"><span class="brand-square"></span><span class="brand-name">KEEN CREST</span></div>
    <p class="front-author">DORIAN PELLOW</p>
  </section>
</main>
</body>
</html>
```